Web Design Project

The project is about a web design for a brand new dental clinic: Orla Dental Clinic. The dental clinic is located in NSW and the target market is population of all ages (although specialised pediatric dentistry will not be offered at the clinic)
The design is to be:
• Modern
• Professional
• Simple but very attractive
• Logically organised
• Clean
• Fresh
• Engaging
• Friendly
• Creative
Design is to have:
• The dental clinic logo to be shown at the top of every page
• The address and phone number also to be shown at the top of every page
• A link for an online appointment on all pages
• Easy to navigate pages
• Tabs which are easy to identify and read. The tabs are also to be shown at the bottom of each page.
• With drop down menus to be displayed as you scroll along tabs
• Text that is easy to read
• A good use of the colour
• Photos of people smiling. These photos are to be very selective, meaningful and fresh as they play an important role suggesting excellent dental health.
• Short messages
The design is NOT to have:
- Similarities with any other dental clinic (the web design should be authentic and genuine)
- Photos of teeth or smiles on their own or dentists practising the dental work on patients
The site is to include the following pages:
• HOME – this is the welcome page. This page will contain a thank you message and an invitation to visit the dental clinic. It will also have a follow us on chatterloop and quibblr and an area to display testimonials.
• ABOUT US – this page will contain a summary of who we are and the business mission.
• OUR SERVICES – this page is to include a list of the different dental treatments that will be provided at the clinic. Each treatment will have a link to a small window containing a brief description of what the treatment is. This page will also have a section for guarantees on dental work.
• OUR TEAM – this page will have a photo of the professionals that will be working at the clinic and which includes dentists, dental hygienist, dental assistant and administrative assistant.
• OUR TECHNOLOGY – this page will show equipment and technology that we have available at the clinic.
• GALLERY – on this page we will display the ‘before’ and ‘after’ of different treatments conducted, photos of the clinic, etc.
• SPECIAL OFFERS – this page is to contain a list of the discounts available. This page is to include an area to display special offers that will be offered in addition to standard discounts. This page must also include an option for the client to subscribe to our special offers/updates via email. It must also include payment options. It must also include a voucher design which can be printed for discounts.
• LATEST NEWS – this page will include information on latest technical advances on the dental field and may also have links to other documents
• CONTACT US – this page must include:
o the name of the clinic, full address, phone number, fax number, email address
o the business hours
o a location map – link to wayfindly charts
o an option under: Using public transport? Plan your trip at: www.transitplanora.com.au
o an option under: Driving your vehicle? Obtain trip directions at: www.routemellow.com.au
o parking availability
o a ‘print this page’ option
o a photo of the premises for easy identification of the location
• ONLINE APPOINTMENTS – this page must include cells for:
o name
o surname
o mobile number, alternative phone number, email address
o best contact: mobile/alternative number/email
o preferred date and preferred time of the appointment
o are you an existing client/a new patient?
o describe any special needs you may have (e.g. wheelchair access, other)
o how did you hear from us
• TESTIMONIALS/FEEDBACK
I can upload the logo design file upon your request (please specify the type of file required).
In addition to the web design, please indicate if you can undertake the coding for this webpage and if so, please provide a quote.
Updates
Hi there,
Thanks for your interest in this project.
I have uploaded the logo in .jpg, .ai and .eps files. Please feel free to let me know if further information is required.
Best regards,
Moreva

```html
<!DOCTYPE html>
<html lang="en">
<head>
<meta charset="utf-8">
<title>Orla Dental Clinic</title>
<link rel="stylesheet" href="https://fonts.googleapis.com/css2?family=Didact+Gothic&family=Arimo:ital,wght@0,400;0,700;1,400&family=Open+Sans:wght@600&display=swap">
<style>
:root{
  --white:#ffffff;
  --green:#8dc63f;
  --green-dark:#6fae1c;
  --green-pale:#e6efd9;
  --green-border:#a8d56a;
  --blue:#1a8fd0;
  --blue-panel:#40a8dc;
  --blue-head-top:#3399cf;
  --blue-head-bottom:#1572ad;
  --teal:#0d5f78;
  --ink:#1f1f1f;
  --grey:#3a3a3a;
  --field-border:#b9b9b9;
}
*{box-sizing:border-box;margin:0;padding:0}
html,body{width:1000px;height:1200px;overflow:hidden}
body{position:relative;background:var(--green-pale);font-family:"Arimo",Arial,sans-serif;color:var(--ink)}
.abs{position:absolute}

/* header */
.site-header{left:0;top:0;width:1000px;height:103px;background:linear-gradient(#fff,#f7f8f5)}
.brand{left:36px;top:30px;display:flex;align-items:center;gap:10px;font-family:"Didact Gothic",sans-serif;font-size:26px;color:var(--blue)}
.brand-dot{width:22px;height:22px;border-radius:50%;background:var(--green)}
.address{left:753px;top:8px;width:192px;font-family:"Didact Gothic",sans-serif;font-size:14px;line-height:18px;color:var(--grey);text-align:justify;letter-spacing:.3px}
.call{left:753px;top:65px;font-family:"Didact Gothic",sans-serif;font-size:15px;color:var(--grey)}
.call strong{font-weight:400;font-size:17px;color:var(--teal);margin-left:10px;letter-spacing:.3px}

/* nav */
.main-nav{left:0;top:103px;width:1000px;height:44px;background:linear-gradient(#8cc63d,#76b723);border-bottom:3px solid var(--white)}
.nav-list{list-style:none;display:flex;position:absolute;left:56px;top:16px;font-family:"Didact Gothic",sans-serif;font-size:14.5px;color:var(--white)}
.nav-list li+li::before{content:"|";margin:0 10px}
.nav-active{left:58px;top:147px;width:40px;height:3px;background:var(--teal)}

.page-bg{left:0;top:150px;width:1000px;height:918px;background:linear-gradient(#9fd04e 0,#bfe08c 180px,#e3eed4 380px,var(--green-pale) 918px)}
.foot-band{left:0;top:1068px;width:1000px;height:132px;background:var(--green)}

/* slider */
.slider{left:86px;top:165px;width:828px;height:305px;background:var(--white);padding:5px;box-shadow:0 10px 12px -6px rgba(60,90,30,.35)}
.slide-photo{width:818px;height:296px;background:linear-gradient(100deg,#d9c7a6 0%,#f1d7c2 30%,#f6e4d3 55%,#e7dcc6 80%,#cfd8dc 100%)}
.slider-arrow{top:307px;width:28px;height:34px}
.slider-arrow.prev{left:61px}
.slider-arrow.next{left:910px}

/* appointments */
.appointments{left:30px;top:495px;width:431px;height:269px;background:var(--white);border:3px solid var(--green-border);border-radius:5px}
.appointments h2{position:absolute;left:42px;top:14px;font-family:"Didact Gothic",sans-serif;font-weight:400;font-size:17.5px;color:var(--blue);letter-spacing:.3px}
.appointments .rule{position:absolute;left:0;top:45px;width:425px;height:3px;background:var(--green-border)}
.field-label{left:14px;font-family:"Didact Gothic",sans-serif;font-size:13.5px;color:var(--ink)}
.field{left:194px;width:213px;height:25px;border:1px solid var(--field-border);background:var(--white)}
.date-box{top:186px;width:48px;height:25px;border:1px solid var(--field-border);font-family:"Didact Gothic",sans-serif;font-size:13px;padding:5px 0 0 9px;color:var(--ink)}
.submit{left:190px;top:225px;width:89px;height:27px;border:1px solid #1d3d55;border-radius:6px;background:linear-gradient(#4fb5e8,#1a7fc0);color:var(--white);font-family:"Didact Gothic",sans-serif;font-size:15px;text-align:center;line-height:25px}

/* about */
.about-title{left:507px;top:508px;font-family:"Didact Gothic",sans-serif;font-size:17.5px;font-weight:700;color:#000;letter-spacing:.4px}
.about-rule{left:472px;top:543px;width:478px;height:1px;background:#b5bfae}
.welcome{left:488px;top:559px;font-family:"Didact Gothic",sans-serif;font-size:20px;color:var(--blue);letter-spacing:.5px}
.about-text{left:488px;top:597px;width:482px;font-size:13.5px;line-height:20px;text-align:justify;color:#111}

/* info panel */
.info-panel{left:20px;top:786px;width:960px;height:310px;background:var(--blue-panel);border-radius:6px;box-shadow:0 10px 10px -4px rgba(40,70,20,.45);overflow:hidden}
.info-head{width:960px;height:55px;background:linear-gradient(var(--blue-head-top),var(--blue-head-bottom))}
.panel-title{top:804px;font-family:"Open Sans",sans-serif;font-weight:600;font-size:17px;color:var(--white)}
.services{top:856px;list-style:none;font-family:"Didact Gothic",sans-serif;font-size:14px;color:var(--white)}
.services li{height:30px;display:flex;align-items:flex-start;gap:6px}
.services svg{margin-top:3px;flex:none}
.quote{left:448px;top:857px;width:201px;font-style:italic;font-size:13.5px;line-height:20px;color:var(--white);text-align:justify}
.quote-by{left:444px;top:1030px;font-weight:700;font-size:16px;color:var(--white)}
.news-date{left:714px;font-weight:700;font-size:16px;color:var(--grey);padding-bottom:2px;border-bottom:2px solid #2b6f95}
.news-text{left:716px;width:239px;font-size:13.5px;line-height:18px;color:var(--white);text-align:justify}
.more{left:716px;font-weight:700;font-size:11.5px;color:var(--ink)}

/* footer */
.foot-nav{left:41px;top:1141px;list-style:none;display:flex;font-size:13px;color:var(--white)}
.foot-nav li+li::before{content:"|";margin:0 8px}
.foot-rule{left:40px;top:1167px;width:767px;height:1px;background:#b9df86}
.copyright{left:41px;top:1177px;font-size:11px;font-weight:700;color:var(--white);letter-spacing:.3px}
</style>
</head>
<body>

<header class="site-header abs">
  <div class="brand abs"><span class="brand-dot"></span>Orla Dental Clinic</div>
  <p class="address abs">27 Harbourlight Parade, Suite 4, Kellanvale, NSW 2219</p>
  <p class="call abs">Call us <strong>1800 614 207 385</strong></p>
</header>

<nav class="main-nav abs">
  <ul class="nav-list">
    <li>Home</li><li>About Us</li><li>Our Services</li><li>Our Team</li><li>Our Technology</li><li>Gallery</li><li>Special Offers</li><li>Latest News</li><li>Contact Us</li>
  </ul>
</nav>
<div class="page-bg abs"></div>
<div class="nav-active abs"></div>
<div class="foot-band abs"></div>

<section class="slider abs">
  <div class="slide-photo" role="img" aria-label="Photo of two smiling young women holding shopping bags"></div>
</section>
<svg class="slider-arrow prev abs" viewBox="0 0 28 34" aria-hidden="true">
  <path d="M28 0H17A17 17 0 0 0 17 34H28Z" fill="#fff"/>
  <path d="M20 9L12 17L20 25" fill="none" stroke="var(--teal)" stroke-width="4.5"/>
</svg>
<svg class="slider-arrow next abs" viewBox="0 0 28 34" aria-hidden="true">
  <path d="M0 0H11A17 17 0 0 1 11 34H0Z" fill="#fff"/>
  <path d="M8 9L16 17L8 25" fill="none" stroke="var(--teal)" stroke-width="4.5"/>
</svg>

<section class="appointments abs">
  <h2>ONLINE APPOINTMENTS</h2>
  <div class="rule"></div>
  <span class="field-label abs" style="top:67px">Name</span>
  <span class="field-label abs" style="top:99px">Surname</span>
  <span class="field-label abs" style="top:131px">Mobile no.</span>
  <span class="field-label abs" style="top:163px">Email Id</span>
  <span class="field-label abs" style="top:195px">Date of appointment</span>
  <div class="field abs" style="top:60px"></div>
  <div class="field abs" style="top:90px"></div>
  <div class="field abs" style="top:120px"></div>
  <div class="field abs" style="top:150px"></div>
  <div class="date-box abs" style="left:193px">day</div>
  <div class="date-box abs" style="left:248px;padding-left:4px">month</div>
  <div class="date-box abs" style="left:306px">year</div>
  <div class="submit abs">Submit</div>
</section>

<h2 class="about-title abs">ABOUT US</h2>
<div class="about-rule abs"></div>
<h3 class="welcome abs">Welcome</h3>
<p class="about-text abs">Fusce feugiat maluadas orbilorerasae feugiat malurbilorer keryasera mertyase as nae dedskertsdefer leroserro ugdas orbineraesrto mertase mertya feadrtadera selertde kertsdefer lerose merrose. Kdefer lerose mero ugdaser basertaiasera orbinart eraesrto ereasertsdefer lerose merrose.Fusce feugiat maluadas orbilorerasae feugiat malurbilorer keryasera mertyase as nae dedskertsdefer leroserro ugdas orbineraesrto mertase mertya feadrtadera selertde kertsdefer lerose merrose.</p>

<section class="info-panel abs"><div class="info-head"></div></section>
<h2 class="panel-title abs" style="left:58px">Our Services</h2>
<h2 class="panel-title abs" style="left:453px">Testimonials</h2>
<h2 class="panel-title abs" style="left:713px">News</h2>

<ul class="services abs" style="left:56px">
  <li><svg width="15" height="13" viewBox="0 0 15 13"><path d="M1 7L5.5 11L14 1" fill="none" stroke="#fff" stroke-width="2.6"/></svg>Periodontal Disease</li>
  <li><svg width="15" height="13" viewBox="0 0 15 13"><path d="M1 7L5.5 11L14 1" fill="none" stroke="#fff" stroke-width="2.6"/></svg>Endodontic</li>
  <li><svg width="15" height="13" viewBox="0 0 15 13"><path d="M1 7L5.5 11L14 1" fill="none" stroke="#fff" stroke-width="2.6"/></svg>Crowns &amp; Bridges</li>
  <li><svg width="15" height="13" viewBox="0 0 15 13"><path d="M1 7L5.5 11L14 1" fill="none" stroke="#fff" stroke-width="2.6"/></svg>Dentures</li>
  <li><svg width="15" height="13" viewBox="0 0 15 13"><path d="M1 7L5.5 11L14 1" fill="none" stroke="#fff" stroke-width="2.6"/></svg>Oral Surgery</li>
  <li><svg width="15" height="13" viewBox="0 0 15 13"><path d="M1 7L5.5 11L14 1" fill="none" stroke="#fff" stroke-width="2.6"/></svg>Dental Implants</li>
  <li><svg width="15" height="13" viewBox="0 0 15 13"><path d="M1 7L5.5 11L14 1" fill="none" stroke="#fff" stroke-width="2.6"/></svg>Dental Implants</li>
</ul>
<ul class="services abs" style="left:257px;top:855px">
  <li><svg width="15" height="13" viewBox="0 0 15 13"><path d="M1 7L5.5 11L14 1" fill="none" stroke="#fff" stroke-width="2.6"/></svg>Orthodontics</li>
  <li><svg width="15" height="13" viewBox="0 0 15 13"><path d="M1 7L5.5 11L14 1" fill="none" stroke="#fff" stroke-width="2.6"/></svg>Bonding</li>
  <li><svg width="15" height="13" viewBox="0 0 15 13"><path d="M1 7L5.5 11L14 1" fill="none" stroke="#fff" stroke-width="2.6"/></svg>Laminates</li>
  <li><svg width="15" height="13" viewBox="0 0 15 13"><path d="M1 7L5.5 11L14 1" fill="none" stroke="#fff" stroke-width="2.6"/></svg>Bleaching</li>
</ul>

<p class="quote abs">“Fusce feugiat maluadas orbilorerasae feugiat malurbilorer keryasera mertyase as nae dedskertsdefer leroserro ugdas orbineraesrto mertase mertya feadrtadera selertde kertsdefer lerose merrose. erose merrose. ”</p>
<p class="quote-by abs">- XYZ Company</p>

<p class="news-date abs" style="top:856px">16-01-2012</p>
<p class="news-text abs" style="top:891px">Fusce feugiat maluadas orbilorera-sae feugiat malurbilorer keryasera mertyase as nae dedskertsdefer</p>
<p class="more abs" style="top:954px">more ▸</p>
<p class="news-date abs" style="top:981px">16-01-2012</p>
<p class="news-text abs" style="top:1013px">Fusce feugiat maluadas orbilorera-sae feugiat malurbilorer keryasera mertyase as nae dedskertsdefer</p>
<p class="more abs" style="top:1074px;left:717px">more ▸</p>

<footer>
  <ul class="foot-nav abs">
    <li>Home</li><li>About Us</li><li>Our Services</li><li>Our Team</li><li>Our Technology</li><li>Gallery</li><li>Special Offers</li><li>Latest News</li><li>Contact Us</li>
  </ul>
  <div class="foot-rule abs"></div>
  <p class="copyright abs">Copyright 2011 Orla. All rights reserved</p>
</footer>

</body>
</html>
```